Lumora, Soft Dew label sticker for cosmetic cream

I'm looking to design a label sticker for my cosmetic brand. The product is called Soft Dew. The brand is called Lumora. I'm looking for a minimalistic, modern design that encapsulates the fact that the product is all natural. Made with 100% organic ingredients, vegan and cruelty free. The motto of the company is " The Healing Power of Nature"

Target Market(s)

Young professionals, 30+, 40+ interested in natural skin care

Industry/Entity Type

Cosmetic

Colors

Designer to choose only greyscale colors for use in the design.

Requirements
Must have
• Modern look, easily remembered but still a touch of nature

```html
<!DOCTYPE html>
<html lang="en">
<head>
<meta charset="utf-8">
<title>Lumora Soft Dew — Label</title>
<link rel="stylesheet" href="https://fonts.googleapis.com/css2?family=Raleway:wght@300;400;500&family=Montserrat:wght@400;700&family=Great+Vibes&display=swap">
<style>
  :root {
    --canvas: #ffffff;
    --grey-edge: #7c7c7c;
    --grey-mid: #9c9c9c;
    --grey-deep: #6b6b6b;
    --grey-text: #5e5e5e;
    --white: #ffffff;
  }
  * { margin: 0; padding: 0; box-sizing: border-box; }
  html, body {
    width: 1200px; height: 1200px; overflow: hidden;
    background: var(--canvas);
  }
  .canvas { position: relative; width: 1200px; height: 1200px; }
  .label {
    position: absolute; left: 40px; top: 320px;
    width: 1120px; height: 559px;
    background: linear-gradient(90deg, var(--grey-edge) 0%, var(--grey-mid) 32%, var(--grey-mid) 68%, var(--grey-edge) 100%);
    overflow: hidden;
    color: var(--white);
  }
  .vine-illustration {
    position: absolute; left: 0; top: 0; width: 420px; height: 559px;
    background: radial-gradient(ellipse 200px 260px at 90px 200px, rgba(255,255,255,0.45) 0%, rgba(255,255,255,0.2) 55%, rgba(255,255,255,0) 100%);
  }
  .motto-band {
    position: absolute; left: 0; top: 201px; width: 100%; height: 47px;
    background: var(--white);
  }
  .motto {
    position: absolute; left: 0; top: 201px; width: 100%; height: 47px;
    text-align: center; line-height: 47px;
    font-family: "Raleway", sans-serif; font-weight: 500;
    font-size: 30px; letter-spacing: 0.5px;
    color: var(--grey-text);
  }
  .brand {
    position: absolute; left: 0; top: 44px; width: 100%;
    text-align: center;
    font-family: "Raleway", sans-serif; font-weight: 300;
    font-size: 90px; letter-spacing: 4px; line-height: 1;
  }
  .product {
    position: absolute; left: 0; top: 139px; width: 100%;
    text-align: center;
    font-family: "Raleway", sans-serif; font-weight: 400;
    font-size: 35px; letter-spacing: 3px; line-height: 1;
  }
  .nature {
    position: absolute; left: 0; top: 287px; width: 100%;
    text-align: center;
    font-family: "Great Vibes", cursive;
    font-size: 88px; line-height: 1;
  }
  .details {
    position: absolute; left: 0; top: 418px; width: 100%;
    text-align: center;
    font-family: "Montserrat", sans-serif; font-weight: 400;
    font-size: 17px; line-height: 25px;
  }
  .details .variant { font-weight: 700; font-size: 19px; margin-bottom: 4px; }
  .details strong { font-weight: 700; font-size: 21px; }
  .volume {
    position: absolute; left: 466px; top: 507px; width: 189px; height: 52px;
    background: var(--grey-deep);
    border-radius: 12px 12px 0 0;
    text-align: center; line-height: 50px;
    font-family: "Montserrat", sans-serif; font-size: 16px;
  }
</style>
</head>
<body>
  <main class="canvas">
    <section class="label">
      <div class="vine-illustration" role="img" aria-label="White line illustration of a leafy vine with heart-shaped leaves curving down the left side"></div>
      <div class="motto-band"></div>
      <p class="motto">THE HEALING POWER OF</p>
      <h1 class="brand">LUMORA</h1>
      <p class="product">SOFT DEW</p>
      <p class="nature">Nature</p>
      <div class="details">
        <p class="variant">DAWN BLOOM</p>
        <p>Made with <strong>100% organic</strong> ingredients</p>
        <p>vegan and cruelty free</p>
      </div>
      <div class="volume">e 30 ml / oz</div>
    </section>
  </main>
</body>
</html>
```